Like us

We need a contest ad that offers a free weekend getaway stay in our Spa Suite- Bridal or Family Suite or King Suite, winners choice. (subject to availability, some conditions apply)
Objective - to encourage existing followers to refer friends and obtain new likes. Each referral "like" should leave a comment with just the referral name in the comment line. We will compile these referral names and the new like names for 1 "referer" weekend getaway package & 1 new "like" weekend getaway package Prize package includes a dinner certificate at the Marlow Hearth (value $ 30) & a complimentary bottle of champagne
(In room or at the Restaurant.) Facebook Contest closes June 30th, 2014. The professional image is the important part of the design, comment lines can be used for contest explanations, however it would be nice to incorporate in the design. Design first!
The Motel Logo is AR Bonnie with a shadow. (bad copy uploaded)

Target Market(s)

Travelers

Industry/Entity Type

Restaurant

Requirements
Must have
• Professional Image
Nice to have
• Explanation of contest

```html
<!DOCTYPE html>
<html lang="en">
<head>
<meta charset="utf-8">
<title>Win a Getaway Weekend – Contest Ad</title>
<link rel="stylesheet" href="https://fonts.googleapis.com/css2?family=Bangers&family=Kaushan+Script&family=Ubuntu:wght@400;700&display=swap">
<style>
  :root {
    --backdrop: #e9e9e9;
    --paper: #ffffff;
    --sky-top: #cfe3f7;
    --sky-mid: #8fbdea;
    --sky-low: #d9e9f8;
    --band: rgba(96, 156, 222, 0.55);
    --ink-white: #ffffff;
    --ink-blue: #2f8fe6;
    --ink-navy: #1d4f9e;
    --pill: #2a5fae;
    --brand-brown: #5a3418;
    --brand-green: #4f7a1f;
    --note: #6d6d6d;
  }
  * { margin: 0; padding: 0; box-sizing: border-box; }
  html, body { width: 1200px; height: 789px; overflow: hidden; background: var(--backdrop); }
  .ad {
    position: absolute; left: 286px; top: 0; width: 628px; height: 789px;
    background: linear-gradient(180deg, var(--sky-top) 14%, var(--sky-mid) 45%, var(--sky-low) 78%, var(--paper) 92%);
    overflow: hidden; font-family: "Ubuntu", sans-serif;
  }
  .header {
    position: absolute; left: 0; top: 0; width: 100%; height: 120px;
    background: linear-gradient(180deg, var(--paper) 80%, rgba(255,255,255,0));
    display: flex; align-items: center; justify-content: space-between; padding: 0 40px 10px 36px;
  }
  .brand { display: flex; align-items: center; gap: 12px; font-family: "Ubuntu", sans-serif; font-weight: 700; font-size: 30px; }
  .brand--motel { color: var(--brand-brown); }
  .brand--grill { color: var(--brand-green); }
  .brand__mark { width: 30px; height: 30px; border-radius: 50%; background: var(--brand-green); }
  .band {
    position: absolute; left: 0; top: 120px; width: 100%; height: 275px;
    background: linear-gradient(180deg, rgba(255,255,255,0.35), var(--band) 40%, rgba(120,175,230,0.2));
  }
  .headline {
    position: absolute; left: 0; top: 130px; width: 100%; text-align: center;
    font-family: "Bangers", sans-serif; font-size: 58px; letter-spacing: 1px; color: var(--ink-white);
    -webkit-text-stroke: 2px var(--ink-navy); transform: skewX(-8deg);
  }
  .rules {
    position: absolute; left: 20px; top: 222px; width: 588px; text-align: center;
    color: var(--ink-white); font-size: 25px; line-height: 33px;
    text-shadow: 0 1px 3px rgba(30,80,150,0.35);
  }
  .prize {
    position: absolute; left: 22px; top: 402px; width: 500px;
    color: var(--ink-blue); font-weight: 700; font-size: 26px; line-height: 34px;
  }
  .deadline {
    position: absolute; left: 0; top: 565px; width: 340px; height: 120px;
    background: var(--pill); border-radius: 0 60px 60px 0;
    padding: 12px 0 0 24px; color: var(--ink-white);
    font-family: "Kaushan Script", cursive; font-size: 36px; line-height: 48px;
  }
  .footnote {
    position: absolute; left: 10px; top: 728px; color: var(--note); font-size: 18px; line-height: 22px;
  }
  .photo-bottle {
    position: absolute; left: 528px; top: 405px; width: 92px; height: 370px;
    border-radius: 30px 30px 6px 6px;
    background: linear-gradient(160deg, #4a3d2c 0%, #1f1a14 55%, #2b231a 100%);
  }
  .photo-glasses {
    position: absolute; left: 410px; top: 545px; width: 112px; height: 230px;
    border-radius: 20px 20px 6px 6px;
    background: linear-gradient(180deg, #e8cf96 0%, #c99a4a 45%, #efe2c4 100%);
    opacity: 0.9;
  }
</style>
</head>
<body>
  <main class="ad">
    <header class="header">
      <div class="brand brand--motel">Ashby's Motel</div>
      <div class="brand brand--grill"><span class="brand__mark"></span>Marlow Hearth</div>
    </header>
    <div class="band"></div>
    <h1 class="headline">Win a Getaway Weekend!</h1>
    <p class="rules">Refer our page to a friend and have them<br>like it &amp; write a comment mentioning<br>your name for a chance to win.<br>1 "referrer" &amp; 1 new "like" weekend<br>getaway package to be given away.</p>
    <p class="prize">Prize package includes a dinner certificate at the Marlow Hearth (value $ 30) &amp; a complimentary bottle of champagne*.</p>
    <div class="deadline">Contest ends<br>June 30th, 2014</div>
    <div class="photo-glasses" role="img" aria-label="Photo of two filled champagne glasses"></div>
    <div class="photo-bottle" role="img" aria-label="Photo of a dark champagne bottle"></div>
    <p class="footnote">* Subject to availability,<br>&nbsp;&nbsp;some conditions apply.</p>
  </main>
</body>
</html>
```